Banner ad for Gen Y demographic - Training Institute

We are a training organization that requires two (2) banner ads which we can use to promote our brand, our Diploma of Management and Diploma of Business product offerings, you may visit our website: www.pembertonvale.com.au to grab some background information on us.

I have also included our logo to be used in the banner ad (white or black depending on background color). The text to be used throughout the banner ad is Times New Roman please.

We require flash banners that just have the text changing from one slide to the next. We want something clean and enticing. We also need a call to action button “Start now” or something similar.

I have included the below just as a guide but welcome any creativity that you believe would fit our market. I encourage you to be creative!

Flash panels:
1 Slide – I don’t take classes. I experience them – are you in?
2 Slide - Unlock your potential excellence today

I need two different banner ads / sizes please:

1. 600px (W) x 120px (H), max file size 150KB, gif, jpeg, swf
2. 300px(w) x 250px(h), max size 150KB, gif, jpeg, swf

Out target audience is Gen Y, they are looking for ways to improve their careers, make more money, or to get a different job at their existing employer. They’re looking for a Diploma in Management or Business that will give them the education and the piece of paper that will allow them to get that job.

I look forward to seeing what you come up with!

Industry/Entity Type

Training

```html
<!DOCTYPE html>
<html lang="en">
<head>
<meta charset="utf-8">
<title>Pemberton Vale &amp; Associates – Banner Set</title>
<link rel="stylesheet" href="https://fonts.googleapis.com/css2?family=Tinos:ital,wght@0,400;0,700;1,400&family=Arimo:wght@400&display=swap">
<style>
  :root {
    --board: #1a1a1a;
    --board-edge: #111111;
    --label: #ffffff;
    --ink-light: #ffffff;
    --ink-dark: #2a1a08;
    --accent-gold: #f2b01e;
    --photo-dark: #140c05;
    --photo-mid: #5a2c0c;
    --photo-warm: #b5601a;
    --photo-glow: #e8a24a;
    --button-light: #f7d77a;
    --button-deep: #c98a1c;
    --crest-fill: rgba(255, 255, 255, 0.9);
  }
  * { margin: 0; padding: 0; box-sizing: border-box; }
  html, body {
    width: 1200px;
    height: 750px;
    overflow: hidden;
  }
  body {
    position: relative;
    background: radial-gradient(ellipse at center, var(--board) 0%, var(--board-edge) 100%);
    font-family: "Tinos", "Times New Roman", serif;
  }
  .size-label {
    position: absolute;
    left: 0;
    width: 1200px;
    text-align: center;
    font-family: "Arimo", Arial, sans-serif;
    font-size: 19px;
    color: var(--label);
    letter-spacing: 0.5px;
  }
  .size-label--leaderboard { top: 52px; }
  .size-label--rectangle { top: 702px; }

  .banner {
    position: absolute;
    overflow: hidden;
    color: var(--ink-light);
  }
  .banner__photo {
    position: absolute;
    inset: 0;
  }
  .banner--wide {
    left: 150px; top: 99px; width: 900px; height: 180px;
  }
  .banner--wide .banner__photo {
    background:
      radial-gradient(ellipse 40% 70% at 78% 35%, var(--photo-glow) 0%, transparent 70%),
      linear-gradient(90deg, var(--photo-dark) 0%, var(--photo-mid) 35%, var(--photo-warm) 70%, var(--photo-mid) 100%);
  }
  .banner--box {
    left: 375px; top: 312px; width: 450px; height: 375px;
  }
  .banner--box .banner__photo {
    background:
      radial-gradient(ellipse 60% 45% at 15% 10%, var(--photo-glow) 0%, transparent 70%),
      linear-gradient(160deg, var(--photo-warm) 0%, var(--photo-mid) 45%, var(--photo-dark) 80%, var(--photo-mid) 100%);
  }
  .banner__shade {
    position: absolute;
    inset: 0;
    background: linear-gradient(180deg, transparent 35%, rgba(0,0,0,0.45) 100%);
  }

  .brand-mark { position: absolute; }
  .banner__text {
    position: absolute;
    white-space: nowrap;
    text-align: center;
    line-height: 1;
  }
  .brand-name { font-weight: 400; }
  .brand-tagline { font-weight: 400; }
  .headline { font-weight: 400; }
  .headline__accent { color: var(--accent-gold); font-style: italic; }

  .cta {
    position: absolute;
    border-radius: 50%;
    background: radial-gradient(circle at 40% 40%, var(--button-light) 0%, var(--button-deep) 100%);
  }
  .cta__label {
    position: absolute;
    font-weight: 700;
    color: var(--ink-dark);
    text-align: center;
    line-height: 1.15;
  }

  /* wide banner positions */
  .banner--wide .brand-mark { left: 84px; top: 16px; }
  .banner--wide .brand-name { left: 220px; top: 20px; width: 480px; font-size: 36px; }
  .banner--wide .brand-tagline { left: 220px; top: 66px; width: 480px; font-size: 18px; }
  .banner--wide .headline--first { left: 200px; top: 96px; width: 500px; font-size: 30px; }
  .banner--wide .headline--second { left: 200px; top: 132px; width: 500px; font-size: 30px; }
  .banner--wide .cta { left: 770px; top: 50px; width: 256px; height: 256px; }
  .banner--wide .cta__label { left: 40px; top: 45px; width: 80px; font-size: 21px; }
  .banner--wide .cta__pointer { position: absolute; left: 16px; top: 60px; }

  /* box banner positions */
  .banner--box .brand-mark { left: 165px; top: 16px; }
  .banner--box .brand-name { left: 0; top: 176px; width: 450px; font-size: 31px; }
  .banner--box .brand-tagline { left: 0; top: 215px; width: 450px; font-size: 17px; }
  .banner--box .headline--first { left: 0; top: 245px; width: 450px; font-size: 28px; }
  .banner--box .headline--second { left: 0; top: 278px; width: 450px; font-size: 28px; }
  .banner--box .headline--third { left: 0; top: 311px; width: 310px; font-size: 28px; }
  .banner--box .cta { left: 333px; top: 258px; width: 234px; height: 234px; }
  .banner--box .cta__label { left: 33px; top: 52px; width: 80px; font-size: 21px; }
</style>
</head>
<body>

  <p class="size-label size-label--leaderboard">600PX X 120PX</p>

  <section class="banner banner--wide">
    <div class="banner__photo" role="img" aria-label="Warm close-up photograph of a leather-bound book spine"></div>
    <div class="banner__shade"></div>
    <svg class="brand-mark" width="120" height="120" viewBox="0 0 120 120" aria-hidden="true">
      <circle cx="60" cy="60" r="54" fill="var(--crest-fill)"/>
    </svg>
    <p class="banner__text brand-name">Pemberton Vale &amp; Associates</p>
    <p class="banner__text brand-tagline">Institute of Business and Management</p>
    <p class="banner__text headline headline--first">I don’t take classes.</p>
    <p class="banner__text headline headline--second">I experience them – <span class="headline__accent">are you in?</span></p>
    <div class="cta">
      <svg class="cta__pointer" width="30" height="30" viewBox="0 0 30 30" aria-hidden="true">
        <polygon points="28,2 2,14 12,17 15,28" fill="#ffffff"/>
      </svg>
      <p class="cta__label">START<br>NOW</p>
    </div>
  </section>

  <section class="banner banner--box">
    <div class="banner__photo" role="img" aria-label="Warm close-up photograph of open book pages"></div>
    <div class="banner__shade"></div>
    <svg class="brand-mark" width="120" height="120" viewBox="0 0 120 120" aria-hidden="true">
      <circle cx="60" cy="60" r="56" fill="var(--crest-fill)"/>
    </svg>
    <p class="banner__text brand-name">Pemberton Vale &amp; Associates</p>
    <p class="banner__text brand-tagline">Institute of Business and Management</p>
    <p class="banner__text headline headline--first">I don’t take classes.</p>
    <p class="banner__text headline headline--second">I experience them</p>
    <p class="banner__text headline headline--third"><span class="headline__accent">– are you in?</span></p>
    <div class="cta">
      <p class="cta__label">START<br>NOW</p>
    </div>
  </section>

  <p class="size-label size-label--rectangle">300PX X 250PX</p>

</body>
</html>
```